Norwegian psychologist service needs a fresh and exiting web site*

Norwegian psychologist service: working with therapy, personal development, mastery and personal growth. Focus: children and teenagers with special needs; family dynamics; group processes; individuals with a need for therapy and personal growth. (Our company name: Fjordlys og samhold (means Mastery and Growth).

We already have a logo for the company, which will be used (will be attached in the project).

The webside is to be structured in 4 pages with roll down curtain menus (the numbers are just for guiding the designer - the should not be added):

Page 1: Om Fjordlys og Samhold (about Mastery and Growth): this is where our business is is presented/described shortly: Lorem Ipsum dolor cit...

Page 2: Tjenester (Services): this is where our 5 service areas are presented:
2.1 Utredning (Investigation, diagnosing): Lorem Ipsum dolor cit...
2.2 Rådgivning (consulting): Lorem Ipsum dolor cit...

2.3 Kurs og work shops (courses and work shops): Lorem Ipsum dolor cit...
2.3a Fjordlys og samhold Tema 1 (T1)
2.3b Fjordlys og samhold Tema 2 (T2)
2.3c Fjordlys og samhold Tema 3 (T3)

2.4 Terapi og utvikling (Therapy and development)
2.4a Fjordlys og samhold for individer (FS1)
2.4b Fjordlys og samhold i familier (FS2)
2.4c Fjordlys og samhold i grupper (FS3)
2.4d Fjordlys og samhold i institusjoner (FS4)

Page 3: Aktuelt (Blog): this is our blog where we share knowledge and articles

Page 4: Kontakt (Contact): This is the contact form page. Contact form should constitute:
- Ditt navn (your name)
- E-post (your e-mail)
- Emne (subject)
- Melding (message/description)

Our project should also include suggestion for handheld units (iPhone, iPad).
Updates

We have both been traveling with work for a while, and then unfortunately both of us got sick on return, so we need a few more days to evaluate and choose design. Kind Regards Arvid & Margit

Target Market(s)

Focus on therapy, learning, mastery and growth for children and teenagers with special needs, within the family dynamics, or in a group setting.
OUR MARKETS:
Private market: individuals, families, groups and health industry institutions (with focus on learning, mastery, growth (as well as growing up) and psychiatry for children and teenagers with special difficulties and needs)
Public institutions: Government institutions, state institutions and municipality institutions (e.g. schools, municipality health service, hospitals) that serve the public (families with children and teenagers with special needs, and where learning, mastery, growth (as well as growing up) and potential psychiatry is an issue).

Number of Pages Required

4 page

Font styles to use
Sans Serif

Colors

Designer to choose colors to be used in the design.

Requirements
Must have
• The website must have 4 pages with roll down curtain menus (we have added a PDF with suggested structure, and headings, with sub menus - see attached PDF drawing.
• The web page must also use the added logo file - and make the web page work well with our logo.
• We would like the website to have a modern look and we would like the site to be associated with typical HIGH END TOP QUALITY private health institutions, but with a stronger focus on human beings (hands, faces etc), and not white coats and doctors. We are psychologists in the private market.
• For instance, if photos are being used - we tend to like "warm" almost art-like, "grainy" two-tone (e.g. sepia) photos to illustrate our focus. If designer can find such photos as part of design, it would be interesting to us. We would like a few photos like that integrated in the design.
• We also want a design suggestion for how the web page should look like and behave on handheld units (e.g. iPhone, iPad).
Nice to have
• If designer could find a number of suitable photos that matches the business idea and design requirements (see description above), that could follow website, that would be good.
• It could also be nice to have graphic symbols that denote the different pages/subpages (subjects)....
• HORSES: we sometimes use horses as a "tool" in therapy sessions. The horse is not necessarily used for riding, but for contact, communication and grooming. PHOTOS: we would like the designer to find an opportunity for using a photo reflecting this cooperation between therapist, child, teenager and horse. It is a bit up to the designer to find a way to do this... Since the horse is only a tool, among many other tools, it does not have to be much - but we want to try and see how it will work with a photo that also reflects this part of our business.

```html
<!DOCTYPE html>
<html lang="en">
<head>
<meta charset="utf-8">
<title>Fjordlys og Samhold – Norwegian Psychologist Service</title>
<link href="https://fonts.googleapis.com/css2?family=Montserrat:wght@300;400;500;600;700&display=swap" rel="stylesheet">
<style>
:root{
  --brand:#3c4797;
  --brand-deep:#353f8c;
  --ink:#1d1d22;
  --text:#4a4a55;
  --dark:#121214;
  --mist:#f6f6f9;
  --bar:#e4e4ea;
  --white:#ffffff;
}
*{box-sizing:border-box;margin:0;padding:0}
html,body{width:1200px;height:3188px;overflow:hidden}
body{position:relative;font-family:'Montserrat',sans-serif;color:var(--text);background:var(--white)}
.abs{position:absolute}

/* hero */
.hero{left:0;top:0;width:1200px;height:560px;
  background:linear-gradient(100deg,#3d4798 0%,#5a5ea6 30%,#a89aae 55%,#d9b89c 72%,#cfb3a3 88%,#8f86b6 100%)}
.hero-figure{left:300px;top:130px;width:870px;height:430px;
  background:radial-gradient(ellipse at 60% 55%,rgba(232,160,60,.85) 0%,rgba(226,170,90,.45) 35%,rgba(220,180,140,0) 70%)}
.topbar{left:0;top:0;width:1200px;height:45px;background:rgba(255,255,255,.18)}
.contact-mini{top:14px;font-size:12.5px;color:var(--ink);display:flex;align-items:center;gap:6px}
.social{display:flex;gap:10px}
.social span{width:28px;height:28px;border:1.5px solid var(--white);border-radius:50%;display:block}
.brand{left:93px;top:58px;width:110px;display:flex;align-items:center;gap:6px;color:var(--brand);font-weight:600;font-size:13px;line-height:1.2}
.brand i{width:22px;height:22px;border-radius:50%;background:var(--brand);flex:none}
.nav{top:76px;right:91px;display:flex;gap:48px;font-size:13px;color:var(--ink);font-weight:500}
.hero h1{left:93px;top:186px;color:var(--white);font-size:48px;line-height:1;font-weight:400}
.hero h1 b{display:block;font-weight:700;font-size:44px;margin-top:2px}
.hero-lede{left:95px;top:288px;width:380px;color:rgba(255,255,255,.9);font-size:15.5px;line-height:22px}
.arrow{top:376px;width:38px;height:38px;border:2px solid var(--white);border-radius:50%}

/* about */
.about-shadow{left:94px;top:693px;width:428px;height:362px;background:#26262a}
.about-photo{left:111px;top:707px;width:428px;height:364px;background:linear-gradient(90deg,#dcdbe0,#cfcfd6 50%,#c8c8cf)}
.about-frame{left:482px;top:660px;width:614px;height:441px;border:12px solid var(--brand)}
.about-title{left:589px;top:780px;font-size:38px;font-weight:700;color:var(--brand)}
.about-text{left:589px;top:842px;width:450px;font-size:11.6px;line-height:18px;color:var(--text)}

/* services */
.service-bg{left:0;top:1188px;width:1200px;height:482px;
  background:linear-gradient(90deg,#f7f7f9 0%,#fbfbfc 45%,#f3ede9 70%,#faf8f7 100%)}
.section-title{width:1200px;left:0;text-align:center;font-size:38px;font-weight:700;color:var(--brand)}
.section-sub{left:0;width:1200px;text-align:center;font-size:11.6px;line-height:18px;color:var(--text)}
.svc{width:340px;text-align:center}
.svc-icon{width:82px;height:82px;border-radius:50%;background:var(--white);margin:0 auto;box-shadow:0 4px 0 var(--brand),0 2px 8px rgba(0,0,0,.12);display:flex;align-items:center;justify-content:center}
.svc h3{font-size:16px;font-weight:600;color:var(--ink);margin-top:22px}
.svc p{font-size:11.6px;line-height:22px;color:var(--ink);margin-top:6px}
.svc p.just{text-align:justify;text-align-last:center;line-height:18px}
.svc em{font-style:normal;color:var(--brand)}

/* blog */
.card{top:1915px;width:327px;height:361px;background:var(--white);box-shadow:0 4px 10px rgba(0,0,0,.12)}
.card-photo{height:200px}
.card-date{margin:16px 14px 0;font-size:12px;color:var(--ink)}
.card h4{margin:14px 13px 0;font-size:17px;font-weight:400;color:var(--ink)}
.card p{margin:12px 15px 0;font-size:11.8px;line-height:18px;color:var(--ink)}

/* contact */
.contact-info{left:94px;top:2384px;width:322px;height:399px;background:var(--brand)}
.contact-form{left:416px;top:2384px;width:690px;height:399px;background:var(--dark)}
.contact h2{font-size:30px;font-weight:700;color:var(--white)}
.info-row{left:49px;display:flex;gap:14px;color:var(--white);font-size:12.5px;line-height:21px}
.field{position:absolute;border:1px solid #9a9aa2;color:#bdbdc4;font-size:11px;padding:13px 15px}
.send{position:absolute;left:55px;top:323px;width:586px;height:41px;background:var(--white);color:var(--brand);font-weight:700;font-size:16px;text-align:center;line-height:41px}

/* footer */
.footer{left:0;top:2876px;width:1200px;height:267px;background:var(--brand)}
.footer-brand{left:0;width:1200px;top:100px;text-align:center;color:var(--white);font-size:32px;font-weight:400;letter-spacing:1px}
.footer-nav{left:0;width:1200px;top:210px;display:flex;justify-content:center;gap:22px;color:var(--white);font-size:13px}
.copy{left:0;top:3143px;width:1200px;height:45px;background:var(--bar);text-align:center;line-height:45px;font-size:10px;color:#666}
.copy b{color:var(--brand);font-weight:500;font-size:12px}
</style>
</head>
<body>

<section class="abs hero">
  <div class="abs hero-figure" role="img" aria-label="Photo of a woman in a mustard sweater with arms spread wide, eyes closed"></div>
  <div class="abs topbar"></div>
  <div class="abs contact-mini" style="left:698px">
    <svg width="12" height="12" viewBox="0 0 24 24"><path d="M6.6 10.8a15 15 0 006.6 6.6l2.2-2.2c.3-.3.7-.4 1-.2 1.1.4 2.3.6 3.6.6.6 0 1 .4 1 1V20c0 .6-.4 1-1 1A17 17 0 013 4c0-.6.4-1 1-1h3.5c.6 0 1 .4 1 1 0 1.3.2 2.5.6 3.6.1.3 0 .7-.2 1z" fill="#1d1d22"/></svg>+47 212 34 567
  </div>
  <div class="abs contact-mini" style="left:838px">
    <svg width="16" height="11" viewBox="0 0 16 11"><rect x=".5" y=".5" width="15" height="10" fill="none" stroke="#1d1d22"/><path d="M.5.5 8 6l7.5-5.5" fill="none" stroke="#1d1d22"/></svg>post@fjordlys.no
  </div>
  <div class="abs social" style="left:998px;top:8px"><span></span><span></span><span></span></div>
  <div class="abs brand"><i></i>Fjordlys og Samhold</div>
  <nav class="abs nav"><span>Home</span><span>About Us</span><span>Service</span><span>Blog</span><span>Contact Us</span></nav>
  <h1 class="abs">Norwegian<b>Psychologist service</b></h1>
  <p class="abs hero-lede">Lorem Ipsum is simply dummy text of the printing and typesetting industry. Lorem Ipsum has been the industry's standard dummy</p>
  <svg class="abs arrow" style="left:95px" viewBox="0 0 38 38"><path d="M22 11l-8 8 8 8" fill="none" stroke="#fff" stroke-width="2"/></svg>
  <svg class="abs arrow" style="left:146px" viewBox="0 0 38 38"><path d="M16 11l8 8-8 8" fill="none" stroke="#fff" stroke-width="2"/></svg>
</section>

<section class="about">
  <div class="abs about-frame"></div>
  <div class="abs about-shadow"></div>
  <div class="abs about-photo" role="img" aria-label="Photo of a therapist taking notes while talking with a client, both seated"></div>
  <h2 class="abs about-title">About Us</h2>
  <p class="abs about-text">Lorem Ipsum is simply dummy text of the printing and typesetting industry. Lorem Ipsum has been the industry's standard dummy text ever since the 1500s, when an unknown printer took a galley of type and scrambled it to make a type specimen book. It has survived not only five centuries, but also the leap into electronic typesetting, remaining essentially unchanged. It was popularised in the 1960s with the release of Tracewell sheets containing Lorem Ipsum passages, and more recently with desktop publishing software like Quillon Layout including versions of Lorem Ipsum</p>
</section>

<section class="services">
  <div class="abs service-bg" role="img" aria-label="Faded background photo of a woman adjusting her glasses"></div>
  <h2 class="abs section-title" style="top:1242px">Service</h2>
  <p class="abs section-sub" style="top:1300px">Aliquam vestibulum at sapien placerat bibendum. Ut cursus risus vel est facilisis, ut rhoncus<br>leo laoreet. Sed laoreet sodales tortor iaculis congue.</p>

  <div class="abs svc" style="left:88px;top:1370px">
    <div class="svc-icon"><svg width="40" height="40" viewBox="0 0 40 40" fill="none" stroke="#1d1d22" stroke-width="1.6"><rect x="4" y="7" width="22" height="16"/><path d="M7 15h4l2-4 3 8 2-4h5"/><path d="M15 23v4M10 28h10"/><rect x="23" y="15" width="12" height="16"/><path d="M26 20h6M26 24h6M26 28h4"/></svg></div>
    <h3>Investigation, diagnosing</h3>
    <p class="just">Aliquam vestibulum at sapien placerat bibendum. Ut cursus risus vel est facilisis, ut rhoncus leo laoreet. Sed laoreet sodales tortor iaculis congue.</p>
  </div>
  <div class="abs svc" style="left:430px;top:1370px">
    <div class="svc-icon"><svg width="40" height="40" viewBox="0 0 40 40" fill="#1d1d22"><circle cx="13" cy="11" r="3.5"/><circle cx="27" cy="11" r="3.5"/><path d="M8 16h10v8H8zM22 16h10v8H22zM4 24h32v3H4zM7 27h3v9H7zM30 27h3v9h-3zM15 27h2v9h-2zM23 27h2v9h-2z"/></svg></div>
    <h3>consulting</h3>
    <p>Aliquam vestibulum at sapien placerat bibendum.<br><em>1.</em> Fjordlys og samhold for individer (FS1) <em>2.</em> Fjordlys og samhold i familier (FS2) <em>3.</em> Fjordlys og samhold i grupper (FS3) Fjordlys og samhold i institusjoner</p>
  </div>
  <div class="abs svc" style="left:782px;top:1370px">
    <div class="svc-icon"><svg width="40" height="40" viewBox="0 0 40 40" fill="none" stroke="#1d1d22" stroke-width="1.8"><rect x="9" y="7" width="22" height="28"/><path d="M12 4v5M16 4v5M20 4v5M24 4v5M28 4v5M13 15h14M13 19h14M13 23h14M13 27h10"/></svg></div>
    <h3>courses and work shops</h3>
    <p>Aliquam vestibulum at sapien placerat bibendum.<br><em>1.</em> Fjordlys og samhold Tema 1 &nbsp;<em>2.</em> Fjordlys og samhold Tema 2<br><em>3.</em> Fjordlys og samhold Tema 3</p>
  </div>
  <svg class="abs" style="left:574px;top:1622px" width="52" height="14" viewBox="0 0 52 14" fill="none" stroke="#3c4797" stroke-width="1.4"><path d="M24 7H2M7 2 2 7l5 5M28 7h22M45 2l5 5-5 5"/></svg>
</section>

<section class="blog">
  <h2 class="abs section-title" style="top:1790px">Blog</h2>
  <p class="abs section-sub" style="top:1846px;font-size:10.5px">Aliquam vestibulum at sapien placerat bibendum. Ut cursus risus vel est facilisis, ut rhoncus leo laoreet. Sed laoreet sodales tortor<br>iaculis congue. Phasellus convallis eros leo, ut luctus mauris interdum eget.</p>

  <article class="abs card" style="left:94px">
    <div class="card-photo" role="img" aria-label="Photo of a counsellor in a yellow armchair talking with a client on a sofa" style="background:linear-gradient(90deg,#e8d36a,#d8d2c8 45%,#bfb9b4)"></div>
    <p class="card-date">Date : 20.02.20</p>
    <h4>Orci varius natoque penatibus</h4>
    <p>Orci varius natoque penatibus et magnis dis parturi-ent montes, nascetur ridiculus mus. Aliquam id ultri-cies sapien.</p>
  </article>
  <article class="abs card" style="left:438px">
    <div class="card-photo" role="img" aria-label="Photo of a psychologist at a desk with a child drawing" style="background:linear-gradient(90deg,#d6d2cc,#eeeeee 55%,#dadde2)"></div>
    <p class="card-date">Date : 20.02.20</p>
    <h4>Orci varius natoque penatibus</h4>
    <p>Orci varius natoque penatibus et magnis dis parturi-ent montes, nascetur ridiculus mus. Aliquam id ultri-cies sapien.</p>
  </article>
  <article class="abs card" style="left:782px">
    <div class="card-photo" role="img" aria-label="Photo of a therapist with a notepad beside a troubled man on a couch" style="background:linear-gradient(90deg,#cfcfcf,#e4e4e4 50%,#9a9a9d)"></div>
    <p class="card-date">Date : 20.02.20</p>
    <h4>Orci varius natoque penatibus</h4>
    <p>Orci varius natoque penatibus et magnis dis parturi-ent montes, nascetur ridiculus mus. Aliquam id ultri-cies sapien.</p>
  </article>
</section>

<section class="contact">
  <div class="abs contact-info">
    <h2 class="abs" style="left:49px;top:50px">Contact Us</h2>
    <div class="abs info-row" style="top:133px"><svg width="14" height="14" viewBox="0 0 24 24"><path d="M6.6 10.8a15 15 0 006.6 6.6l2.2-2.2c.3-.3.7-.4 1-.2 1.1.4 2.3.6 3.6.6.6 0 1 .4 1 1V20c0 .6-.4 1-1 1A17 17 0 013 4c0-.6.4-1 1-1h3.5c.6 0 1 .4 1 1 0 1.3.2 2.5.6 3.6.1.3 0 .7-.2 1z" fill="#fff"/></svg>+47 212 34 567</div>
    <div class="abs info-row" style="top:174px"><svg width="16" height="14" viewBox="0 0 16 11"><rect x=".5" y=".5" width="15" height="10" fill="none" stroke="#fff"/><path d="M.5.5 8 6l7.5-5.5" fill="none" stroke="#fff"/></svg>post@fjordlys.no</div>
    <div class="abs info-row" style="top:214px"><svg width="14" height="18" viewBox="0 0 14 18"><path d="M7 0a7 7 0 00-7 7c0 5 7 11 7 11s7-6 7-11a7 7 0 00-7-7z" fill="#fff"/><circle cx="7" cy="7" r="2.5" fill="#3c4797"/></svg><span>14 Lindeveien, Sandvika,<br>1337, lorem ipsum</span></div>
    <div class="abs social" style="left:49px;top:288px"><span></span><span></span><span></span></div>
  </div>
  <div class="abs contact-form">
    <h2 class="abs" style="left:52px;top:50px">Get un Touch</h2>
    <div class="field" style="left:55px;top:105px;width:288px;height:42px">your name</div>
    <div class="field" style="left:352px;top:105px;width:288px;height:42px">your e-mail</div>
    <div class="field" style="left:55px;top:158px;width:586px;height:41px">subject</div>
    <div class="field" style="left:55px;top:211px;width:586px;height:102px">message</div>
    <div class="send">Send Now</div>
  </div>
</section>

<footer>
  <div class="abs footer">
    <div class="abs footer-brand">FJORDLYS OG SAMHOLD</div>
    <nav class="abs footer-nav"><span>Home</span><span>I</span><span>About Us</span><span>I</span><span>Service</span><span>I</span><span>Blog</span><span>I</span><span>Contact Us</span></nav>
  </div>
  <div class="abs copy">©2020 <b>FJORDLYS OG SAMHOLD</b>.All rights reserved</div>
</footer>

</body>
</html>
```